Lotus Nest Product Marketing Sheet Front and Back

Please see the VERY VERY VERY ROUGH COMPS THAT WE DID TO LEND SOME DIRECTION TO THE PIECE- SO YOU HAVE AN IDEA OF WHAT'S IMPORTANT TO COMMUNICATE ON THE FRONT AND THE BACK.

DON'T FOLLOW OUR LAYOUT.. This is just for you to see what goes to the front and what goes to the back.. see the files that we just loaded up to the art folder!

We also have a PDF that has a check off list for items that need to be on the front and then on the back!

PROJECT SCOPE:

Project is to make a sell sheet front that is 8.5 inches wide x 11 inches tall in a 4 color design using our current Lotus Nest Logo with your design talents. We also need the back of the sell sheet that has the basic instructions on how to install the Lotus Nest Mattress Cover and shows the value added aspects of the product.

We need files in layered PSD format as we have various dealers that we tweak parts of our product line. We will also use these layered files as a back up for the printer in case they don't have the printer font, we can make him print ready file from your PSD file.

We have the logo, tag line, header main font selected and need you to design the look and feel of the piece.

We have all of the copy for the sell sheet- this is the only PDF file in the art file resources.

Overall this piece needs to convey a FUN, FRESH and PEACEFUL PRODUCT.. we don't want a cluttered design.

Updates

Reason: We have a lot of designers that have requested a few more days to submit.. so we are extending the competition. Thank you and good luck!

Target Market(s)

Shopwell Consumers that are buying a mattress cover for comfort, peace of mind and to reduce night heat issues ( sweating) and to avoid dust mites, bed bugs and stains.

Industry/Entity Type

Marketing

Font styles to use
Sans Serif

Colors
f37122
f68e4e
fabb94
0393ce
33a6d7
86cae7
ffffff
add136
fbee3d

Requirements
Must have
• Our Current Logo as the center piece..
• LOTUS NEST is the brand name
• For a peaceful night sleep is the tag line
• Value Points ( see the PDF attached)
• Crisp color, Clean Fonts, Cant be cluttered.
• File Construction- Must be a PSD file 8.5 x11 and 300 DPI for printing
Nice to have
• Clean, Easy to Read and consistent from the front to the back
Should not have
• We don't want a cluttered look and feel for this marketing piece.

```html
<!DOCTYPE html>
<html lang="en">
<head>
<meta charset="utf-8">
<title>Lotus Nest Terry Cloth Waterproof Mattress Protector</title>
<link rel="stylesheet" href="https://fonts.googleapis.com/css2?family=Montserrat:wght@800;900&family=Nunito:wght@700;800;900&display=swap">
<style>
  :root {
    --orange: #f37122;
    --orange-mid: #f68e4e;
    --orange-soft: #fabb94;
    --blue: #0393ce;
    --blue-mid: #33a6d7;
    --blue-soft: #86cae7;
    --white: #ffffff;
    --green: #add136;
    --yellow: #fbee3d;
    --badge-text: #5f8f1f;
    --badge-fill: #eef6c8;
  }
  * { box-sizing: border-box; margin: 0; padding: 0; }
  html, body { width: 930px; height: 1200px; overflow: hidden; background: var(--white); }
  .sheet {
    position: relative;
    width: 930px;
    height: 1200px;
    overflow: hidden;
    background: var(--white);
    font-family: "Nunito", sans-serif;
  }
  .hero-photo {
    position: absolute;
    left: 0; top: 0;
    width: 930px; height: 760px;
    background:
      radial-gradient(ellipse 420px 140px at 640px 520px, #f2f2f4 0%, rgba(242,242,244,0) 100%),
      radial-gradient(ellipse 260px 200px at 330px 560px, #b98366 0%, #8a5a42 45%, rgba(138,90,66,0) 100%),
      radial-gradient(ellipse 420px 120px at 220px 640px, #ffffff 0%, rgba(255,255,255,0) 100%),
      linear-gradient(180deg, #7fc3ea 0%, #bfe3f6 30%, #e7f4fb 50%, #f4f6f8 100%);
  }
  .brand {
    position: absolute;
    left: 92px; top: 60px;
    width: 360px;
    display: flex; flex-direction: column; align-items: center;
  }
  .brand-mark {
    width: 150px; height: 150px;
    border-radius: 50%;
    background: var(--orange-soft);
  }
  .brand-name {
    margin-top: 22px;
    font-family: "Nunito", sans-serif;
    font-weight: 900;
    font-size: 44px;
    letter-spacing: 2px;
    color: var(--orange);
  }
  .tagline {
    position: absolute;
    left: 48px; top: 298px;
    font-weight: 800;
    font-size: 37px;
    color: var(--blue);
    transform: rotate(-6deg);
    transform-origin: left center;
    white-space: nowrap;
  }
  .headline {
    position: absolute;
    right: 42px; top: 42px;
    text-align: center;
    font-family: "Montserrat", sans-serif;
    font-weight: 900;
    color: var(--blue);
    line-height: 1;
  }
  .headline .line-premium { font-size: 64px; letter-spacing: 3px; }
  .headline .line-terry { font-size: 47px; margin-top: 6px; }
  .headline .line-waterproof { font-size: 47px; margin-top: 4px; }
  .headline .line-protector { font-size: 27px; font-weight: 800; margin-top: 8px; letter-spacing: 1px; }
  .fit-tag {
    position: absolute;
    left: 570px; top: 262px;
    width: 350px; height: 90px;
    border-radius: 14px 0 0 14px;
    background: var(--yellow);
    padding: 8px 0 8px 8px;
  }
  .fit-tag span {
    display: flex; align-items: center; justify-content: center;
    width: 100%; height: 100%;
    border-radius: 10px 0 0 10px;
    border: 3px solid var(--white);
    border-right: none;
    background: var(--blue);
    color: var(--white);
    font-family: "Montserrat", sans-serif;
    font-weight: 800;
    font-size: 40px;
    letter-spacing: 1px;
  }
  .band { position: absolute; left: 0; top: 0; width: 930px; height: 1200px; }
  .feature {
    position: absolute;
    display: flex; align-items: center; justify-content: center;
    text-align: center;
    color: var(--badge-text);
    font-weight: 900;
    font-size: 19px;
    line-height: 1.15;
  }
  .feature svg { position: absolute; inset: 0; width: 100%; height: 100%; }
  .feature span { position: relative; }
  .feature-sides { left: 44px; top: 690px; width: 168px; height: 96px; }
  .feature-corners { left: 212px; top: 684px; width: 176px; height: 118px; }
  .feature-noslip { left: 390px; top: 712px; width: 174px; height: 106px; }
  .fabric-detail {
    position: absolute;
    left: 636px; top: 560px;
    width: 250px; height: 250px;
    border-radius: 50%;
    border: 8px solid var(--white);
    box-shadow: 0 0 0 6px var(--yellow);
    background: radial-gradient(circle at 40% 40%, #ffffff 0%, #e9ecef 60%, #c9ced4 100%);
  }
  .detail-arrow { position: absolute; left: 540px; top: 690px; width: 150px; height: 110px; }
  .protects-title {
    position: absolute;
    left: 0; top: 868px; width: 930px;
    text-align: center;
    font-weight: 900;
    font-size: 30px;
    color: var(--orange);
    letter-spacing: 0.5px;
  }
  .threats {
    position: absolute;
    left: 40px; top: 912px;
    width: 850px;
    display: flex; justify-content: space-between;
    list-style: none;
  }
  .threat {
    position: relative;
    width: 130px; height: 130px;
    border-radius: 50%;
    background: var(--orange);
    box-shadow: 0 0 0 3px var(--orange-soft);
  }
  .threat-photo {
    position: absolute;
    left: 17px; top: 10px;
    width: 96px; height: 84px;
    border-radius: 50% 50% 40% 40%;
  }
  .threat-label {
    position: absolute;
    left: 0; bottom: 18px; width: 100%;
    text-align: center;
    color: var(--white);
    font-weight: 900;
    font-size: 14px;
    letter-spacing: 0.5px;
  }
  .photo-fluids { background: radial-gradient(circle, #f2f4f5, #b9c3c8); }
  .photo-mites { background: radial-gradient(circle, #b8a57d, #4b5a3e); }
  .photo-bugs { background: radial-gradient(circle, #c9703c, #f3d6b7); }
  .photo-bacteria { background: radial-gradient(circle, #8fd2d9, #245c6e); }
  .photo-allergens { background: radial-gradient(circle, #b8b3a9, #3e3a3a); }
  .benefits-strip {
    position: absolute;
    left: 0; top: 1052px;
    width: 930px; height: 148px;
    background: linear-gradient(180deg, #f6f08a 0%, var(--yellow) 100%);
  }
  .benefits {
    position: absolute;
    left: 46px; top: 1072px;
    width: 840px;
    display: flex; justify-content: space-between;
    list-style: none;
  }
  .benefit {
    width: 132px;
    display: flex; flex-direction: column; align-items: center;
  }
  .benefit svg { width: 60px; height: 60px; }
  .benefit-label {
    margin-top: 16px;
    font-weight: 900;
    font-size: 13px;
    color: var(--blue);
    white-space: nowrap;
  }
</style>
</head>
<body>
<main class="sheet">
  <div class="hero-photo" role="img" aria-label="Woman sleeping peacefully on a white pillow beneath a soft blue sky with clouds"></div>

  <svg class="band" viewBox="0 0 930 1200" aria-hidden="true">
    <path d="M0 640 Q420 600 930 548 L930 566 Q420 618 0 660 Z" fill="var(--yellow)" opacity="0.8"/>
    <path d="M0 656 Q420 614 930 562 L930 820 Q470 840 0 872 Z" fill="var(--green)"/>
    <path d="M0 860 Q470 826 930 808 L930 1200 L0 1200 Z" fill="var(--white)"/>
  </svg>

  <header class="brand">
    <div class="brand-mark"></div>
    <div class="brand-name">LOTUS NEST</div>
  </header>
  <p class="tagline">For a peaceful nights sleep</p>

  <h1 class="headline">
    <div class="line-premium">PREMIUM</div>
    <div class="line-terry">TERRY CLOTH</div>
    <div class="line-waterproof">WATERPROOF</div>
    <div class="line-protector">MATTRESS PROTECTOR</div>
  </h1>
  <div class="fit-tag"><span>FITS CAL KING</span></div>

  <div class="feature feature-sides">
    <svg viewBox="0 0 168 96" preserveAspectRatio="none"><path d="M20 90 Q0 88 6 66 Q-2 44 20 40 Q24 14 52 18 Q70 0 96 12 Q124 2 138 26 Q166 30 160 56 Q168 84 142 90 Z" fill="var(--badge-fill)" stroke="#d8e99a" stroke-width="2"/></svg>
    <span>5 SIDED<br>PROTECTION</span>
  </div>
  <div class="feature feature-corners">
    <svg viewBox="0 0 176 118" preserveAspectRatio="none"><path d="M22 110 Q0 106 8 82 Q-2 54 22 48 Q24 18 56 20 Q74 0 102 12 Q132 2 146 28 Q174 34 168 64 Q176 102 148 110 Z" fill="var(--badge-fill)" stroke="#d8e99a" stroke-width="2"/></svg>
    <span>ELASTIC<br>CORNERS FOR<br>EXTRA GRIP</span>
  </div>
  <div class="feature feature-noslip">
    <svg viewBox="0 0 174 106" preserveAspectRatio="none"><path d="M22 100 Q0 96 8 74 Q-2 48 22 44 Q24 16 56 18 Q74 0 100 12 Q130 2 144 26 Q172 32 166 60 Q174 94 146 100 Z" fill="var(--badge-fill)" stroke="#d8e99a" stroke-width="2"/></svg>
    <span>NO SLIP<br>MATTRESS<br>PROTECTION</span>
  </div>

  <div class="fabric-detail" role="img" aria-label="Close-up of the white terry cloth protector fitted on a mattress corner"></div>
  <svg class="detail-arrow" viewBox="0 0 150 110" aria-hidden="true">
    <path d="M140 8 Q132 70 48 72" fill="none" stroke="var(--blue)" stroke-width="14" stroke-linecap="round"/>
    <path d="M56 46 L20 74 L58 100 Z" fill="var(--blue)"/>
  </svg>

  <h2 class="protects-title">PROTECTS AGAINST</h2>
  <ul class="threats">
    <li class="threat"><div class="threat-photo photo-fluids" role="img" aria-label="Glass spilling liquid"></div><span class="threat-label">FLUIDS</span></li>
    <li class="threat"><div class="threat-photo photo-mites" role="img" aria-label="Magnified dust mite"></div><span class="threat-label">DUST MITES</span></li>
    <li class="threat"><div class="threat-photo photo-bugs" role="img" aria-label="Bed bug close-up"></div><span class="threat-label">BED BUGS</span></li>
    <li class="threat"><div class="threat-photo photo-bacteria" role="img" aria-label="Magnified bacteria"></div><span class="threat-label">BACTERIA</span></li>
    <li class="threat"><div class="threat-photo photo-allergens" role="img" aria-label="Magnified allergen particle"></div><span class="threat-label">ALLERGENS</span></li>
  </ul>

  <div class="benefits-strip"></div>
  <ul class="benefits">
    <li class="benefit">
      <svg viewBox="0 0 60 60" aria-hidden="true"><circle cx="30" cy="30" r="26" fill="none" stroke="var(--blue)" stroke-width="4"/><path d="M17 25 H24 L33 17 V43 L24 35 H17 Z" fill="var(--blue)"/><line x1="12" y1="12" x2="48" y2="48" stroke="var(--blue)" stroke-width="4"/></svg>
      <span class="benefit-label">QUITE - NO NOISE</span>
    </li>
    <li class="benefit">
      <svg viewBox="0 0 60 60" aria-hidden="true"><circle cx="30" cy="30" r="26" fill="none" stroke="var(--blue)" stroke-width="4"/><path d="M18 38 Q12 38 13 32 Q14 27 20 28 Q21 20 29 20 Q37 20 38 27 Q46 26 46 33 Q46 38 40 38 Z" fill="none" stroke="var(--blue)" stroke-width="3.5" stroke-linejoin="round"/></svg>
      <span class="benefit-label">ULTRA SOFT</span>
    </li>
    <li class="benefit">
      <svg viewBox="0 0 60 60" aria-hidden="true"><circle cx="30" cy="30" r="26" fill="none" stroke="var(--blue)" stroke-width="4"/><path d="M24 16 Q18 26 18 30 A6 6 0 0 0 30 30 Q30 26 24 16 Z M37 26 Q33 33 33 36 A4.5 4.5 0 0 0 42 36 Q42 33 37 26 Z" fill="var(--blue)"/><line x1="12" y1="12" x2="48" y2="48" stroke="var(--blue)" stroke-width="4"/></svg>
      <span class="benefit-label">WATERPROOF</span>
    </li>
    <li class="benefit">
      <svg viewBox="0 0 60 60" aria-hidden="true"><circle cx="30" cy="30" r="26" fill="none" stroke="var(--blue)" stroke-width="4"/><rect x="19" y="16" width="22" height="28" rx="3" fill="none" stroke="var(--blue)" stroke-width="3"/><line x1="19" y1="22" x2="41" y2="22" stroke="var(--blue)" stroke-width="2.5"/><circle cx="30" cy="33" r="6.5" fill="var(--blue)"/></svg>
      <span class="benefit-label">WASHABLE</span>
    </li>
    <li class="benefit">
      <svg viewBox="0 0 60 60" aria-hidden="true"><circle cx="30" cy="30" r="26" fill="none" stroke="var(--blue)" stroke-width="4"/><ellipse cx="30" cy="32" rx="8" ry="10" fill="var(--blue)"/><circle cx="30" cy="20" r="4" fill="var(--blue)"/><path d="M22 28 L15 24 M22 34 L14 35 M38 28 L45 24 M38 34 L46 35" stroke="var(--blue)" stroke-width="2.5"/><line x1="12" y1="12" x2="48" y2="48" stroke="var(--blue)" stroke-width="4"/></svg>
      <span class="benefit-label">NO DUST MITES</span>
    </li>
    <li class="benefit">
      <svg viewBox="0 0 60 60" aria-hidden="true"><circle cx="30" cy="30" r="26" fill="none" stroke="var(--blue)" stroke-width="4"/><circle cx="30" cy="30" r="8" fill="var(--blue)"/><path d="M30 16 V22 M30 38 V44 M16 30 H22 M38 30 H44 M20 20 L24 24 M36 36 L40 40 M40 20 L36 24 M24 36 L20 40" stroke="var(--blue)" stroke-width="3" stroke-linecap="round"/><line x1="12" y1="12" x2="48" y2="48" stroke="var(--blue)" stroke-width="4"/></svg>
      <span class="benefit-label">ALLERGEN FREE</span>
    </li>
  </ul>
</main>
</body>
</html>
```